Business Cards that are elegant and wow

I want to create and print business cards that represent my brand and stand out from the rest. We want to ensure they stay in our branding and the integrity is not lost. I am happy to look at different shapes like square etc.

It will be printed on very thick cards and will be stylish .

I want to create and print business cards that represent my brand and stand out from the rest. We want to ensure they stay in ur branding and the integrity is not lost. I am happy to look at different shapes like square etc.

Target Market(s)

real estate professionals

Industry/Entity Type

Real Estate

Contact Information for Business Card

Maren Holt
hello@brightfernrealty.com.au
brightfernrealty.com.au
0487 316 252 (SMS)

Colors

Designer to choose colors to be used in the design.

Requirements
Must have
• My logo
• email
• website
• Name
Nice to have
• I like the idea of printing with foil or spot gloss. You want it to stand out in a sea.
Should not have
• I would like you to stay in my colour themes. Don't change the colour of my logo

```html
<!DOCTYPE html>
<html lang="en">
<head>
<meta charset="utf-8">
<title>Bright Fern Realty – Business Cards</title>
<link rel="stylesheet" href="https://fonts.googleapis.com/css2?family=Montserrat:wght@300;600;700&family=Open+Sans:wght@400;600&display=swap">
<style>
  :root {
    --backdrop: #e4e6ea;
    --navy-deep: #0a2740;
    --navy: #123f62;
    --paper: #ffffff;
    --paper-shade: #eef0f2;
    --cyan: #2aa8e0;
    --pink: #e5287b;
    --white: #ffffff;
  }
  * { box-sizing: border-box; margin: 0; padding: 0; }
  html, body { width: 1200px; height: 900px; overflow: hidden; }
  body {
    background: var(--backdrop);
    font-family: "Open Sans", sans-serif;
    position: relative;
  }
  .card {
    position: absolute;
    top: 220px;
    width: 460px;
    height: 460px;
    border-radius: 26px;
    box-shadow: 0 18px 40px rgba(0,0,0,0.18);
    overflow: hidden;
  }
  .card--front {
    left: 110px;
    background: radial-gradient(circle at 45% 40%, var(--navy) 0%, var(--navy-deep) 80%);
  }
  .card--back {
    left: 630px;
    background: radial-gradient(circle at 70% 30%, var(--paper) 0%, var(--paper-shade) 100%);
  }
  .brand {
    position: absolute;
    display: flex;
    align-items: center;
    gap: 12px;
  }
  .brand__dot {
    width: 44px;
    height: 44px;
    border-radius: 50%;
    border: 4px solid var(--pink);
    flex: none;
  }
  .brand__name {
    font-family: "Montserrat", sans-serif;
    font-weight: 600;
    font-size: 30px;
    letter-spacing: 0.5px;
    color: var(--cyan);
    white-space: nowrap;
  }
  .card--front .brand { left: 50%; top: 190px; transform: translateX(-50%); }
  .card--back .brand { left: 50%; top: 52px; transform: translateX(-50%); }
  .card--back .brand__dot { width: 40px; height: 40px; }
  .card--back .brand__name { font-size: 27px; }
  .front__web {
    position: absolute;
    left: 0; right: 0;
    bottom: 62px;
    text-align: center;
    color: var(--white);
    font-size: 19px;
    letter-spacing: 5px;
  }
  .contact {
    position: absolute;
    left: 44px;
    bottom: 46px;
  }
  .contact__name {
    font-family: "Montserrat", sans-serif;
    font-size: 34px;
    color: var(--cyan);
    letter-spacing: 1px;
    margin-bottom: 16px;
  }
  .contact__name .first { font-weight: 300; }
  .contact__name .last { font-weight: 700; }
  .contact__list { list-style: none; }
  .contact__item {
    display: flex;
    align-items: center;
    gap: 12px;
    font-size: 18px;
    color: var(--cyan);
    line-height: 1;
    margin-top: 12px;
  }
  .contact__icon { width: 20px; height: 20px; flex: none; }
</style>
</head>
<body>

  <section class="card card--front" aria-label="Card front">
    <div class="brand">
      <span class="brand__dot"></span>
      <span class="brand__name">BRIGHT FERN REALTY</span>
    </div>
    <p class="front__web">brightfernrealty.com.au</p>
  </section>

  <section class="card card--back" aria-label="Card back">
    <div class="brand">
      <span class="brand__dot"></span>
      <span class="brand__name">BRIGHT FERN REALTY</span>
    </div>
    <div class="contact">
      <h1 class="contact__name"><span class="first">MAREN</span> <span class="last">HOLT</span></h1>
      <ul class="contact__list">
        <li class="contact__item">
          <svg class="contact__icon" viewBox="0 0 20 20" aria-hidden="true">
            <rect x="1" y="4" width="18" height="12" fill="var(--pink)"/>
            <path d="M1 4 L10 11 L19 4" fill="none" stroke="#fff" stroke-width="1.5"/>
          </svg>
          hello@brightfernrealty.com.au
        </li>
        <li class="contact__item">
          <svg class="contact__icon" viewBox="0 0 20 20" aria-hidden="true" fill="none" stroke="var(--pink)" stroke-width="1.5">
            <circle cx="10" cy="10" r="8.5"/>
            <ellipse cx="10" cy="10" rx="3.5" ry="8.5"/>
            <line x1="1.5" y1="10" x2="18.5" y2="10"/>
            <line x1="3" y1="5.5" x2="17" y2="5.5"/>
            <line x1="3" y1="14.5" x2="17" y2="14.5"/>
          </svg>
          brightfernrealty.com.au
        </li>
        <li class="contact__item">
          <svg class="contact__icon" viewBox="0 0 20 20" aria-hidden="true" fill="none" stroke="var(--pink)" stroke-width="1.8">
            <rect x="5" y="1.5" width="10" height="17" rx="2"/>
            <line x1="8.5" y1="15.5" x2="11.5" y2="15.5"/>
          </svg>
          0487 316 252 (SMS)
        </li>
      </ul>
    </div>
  </section>

</body>
</html>
```